Restaurant Facility Equipment & Store Maintenance/

I need a flyer showing commercial/industrial kitchen equipment photos we work on Hot Equipment & Cold Equipment and offer many services. see attached highlights

```html
<!DOCTYPE html>
<html lang="en">
<head>
<meta charset="utf-8">
<title>Restaurant Facility Equipment &amp; Store Maintenance Flyer</title>
<link href="https://fonts.googleapis.com/css2?family=Poppins:wght@400;500;600;700;800&display=swap" rel="stylesheet">
<style>
  :root {
    --yellow: #f8d112;
    --ink: #1c1c1c;
    --dark: #232323;
    --dark-2: #141414;
    --white: #ffffff;
    --stage: #d7dadd;
  }
  * { box-sizing: border-box; margin: 0; padding: 0; }
  html, body { width: 1200px; height: 947px; overflow: hidden; }
  body { background: var(--stage); font-family: "Poppins", sans-serif; color: var(--ink); position: relative; }

  .flyer {
    position: absolute; top: 132px;
    width: 880px; height: 1232px;
    transform: scale(0.5545); transform-origin: 0 0;
    overflow: hidden; background: var(--white);
    box-shadow: 0 6px 18px rgba(0,0,0,.18);
  }
  .flyer--front { left: 92px; }
  .flyer--services { left: 621px; }
  .flyer > * { position: absolute; }

  .backdrop { inset: 0; width: 880px; height: 1232px; }
  .line-y { background: var(--yellow); }
  .line-k { background: var(--ink); }

  .photo {
    border: 8px solid var(--white);
    box-shadow: 0 6px 16px rgba(0,0,0,.35);
    background: linear-gradient(135deg, #cfd2d4 0%, #8a8f93 45%, #3d4043 100%);
  }
  .portrait {
    left: 549px; top: 41px; width: 280px; height: 397px;
    background: linear-gradient(160deg, #3f5f8f 0%, #2f5a9c 50%, #2a3b55 100%);
    opacity: .92;
  }

  .headline { left: 67px; top: 62px; color: var(--white); font-weight: 600; line-height: 1; white-space: nowrap; }
  .headline .small { font-size: 50px; letter-spacing: -.5px; display: block; }
  .headline .big { font-size: 60px; font-weight: 800; color: var(--yellow); letter-spacing: -1px; display: block; margin-top: 10px; }
  .headline .small.last { margin-top: 8px; }
  .intro { left: 67px; top: 318px; color: var(--white); font-size: 21px; line-height: 26px; font-weight: 500; }
  .intro em { font-style: normal; color: var(--yellow); }

  .handle { right: 52px; top: 442px; text-align: right; font-size: 31px; font-weight: 700; line-height: 39px; white-space: nowrap; }
  .offer-title { right: 48px; top: 565px; font-size: 44px; font-weight: 800; white-space: nowrap; }

  .offer-item {
    display: flex; align-items: center; justify-content: flex-end; gap: 8px;
    font-size: 20px; font-weight: 600; line-height: 24px; text-align: right; white-space: nowrap;
  }
  .offer-item svg { width: 20px; height: 20px; flex: none; }
  .col-a { right: 275px; }
  .col-b { right: 52px; }

  .need { text-align: right; font-weight: 800; font-size: 38px; line-height: 44px; white-space: nowrap; }
  .need .accent { color: var(--yellow); display: block; }
  .call-pill {
    left: 604px; top: 1008px; width: 208px; height: 46px; border-radius: 23px;
    background: var(--yellow); color: var(--white); font-weight: 800; font-size: 37px;
    display: flex; align-items: center; justify-content: center;
  }
  .call-note { right: 72px; top: 1066px; text-align: right; font-size: 21px; line-height: 26px; font-weight: 500; white-space: nowrap; }

  .contact { display: flex; align-items: center; gap: 10px; }
  .contact svg { width: 56px; height: 56px; flex: none; }
  .contact .label { color: var(--yellow); font-size: 23px; font-weight: 600; line-height: 1; display: block; }
  .contact .number { font-size: 42px; font-weight: 700; line-height: 1.05; display: block; white-space: nowrap; }

  .services-pill {
    left: 292px; top: 30px; width: 296px; height: 48px; border-radius: 24px;
    background: var(--yellow); font-weight: 800; font-size: 33px;
    display: flex; align-items: center; justify-content: center; white-space: nowrap;
  }
  .service-list { list-style: none; color: var(--white); font-size: 19px; line-height: 27px; font-weight: 400; }
  .service-list li { position: relative; padding-left: 16px; margin-bottom: 17px; white-space: nowrap; }
  .service-list li::before {
    content: ""; position: absolute; left: 0; top: 11px;
    width: 7px; height: 7px; border-radius: 50%; background: var(--yellow);
  }
  .list-left { left: 58px; top: 98px; }
  .list-right { left: 470px; top: 98px; }

  .repair-row { display: flex; align-items: center; gap: 12px; font-size: 31px; font-weight: 700; line-height: 1; white-space: nowrap; }
  .repair-row svg { width: 30px; height: 28px; flex: none; }
  .repair-row .pair { display: flex; align-items: center; gap: 12px; margin-left: 22px; }
  .fix-note { left: 485px; top: 953px; font-size: 23px; font-weight: 800; line-height: 31px; white-space: nowrap; }

  .flyer--services .contact svg { width: 50px; height: 50px; }
  .flyer--services .contact .number { font-size: 37px; }
</style>
</head>
<body>

<!-- FRONT -->
<section class="flyer flyer--front">
  <svg class="backdrop" viewBox="0 0 880 1232" preserveAspectRatio="none" role="img" aria-label="Dimmed commercial kitchen photo behind the heading">
    <defs>
      <linearGradient id="front-dark" x1="0" y1="0" x2="1" y2="1">
        <stop offset="0" stop-color="#2b2b2b"/><stop offset="1" stop-color="#151515"/>
      </linearGradient>
    </defs>
    <rect width="880" height="1232" fill="url(#front-dark)"/>
    <polygon points="0,512 880,407 880,847 0,957" fill="#f8d112"/>
    <polygon points="0,957 880,847 880,1232 0,1232" fill="#ffffff"/>
  </svg>

  <div class="line-y" style="left:35px;top:35px;width:582px;height:2px"></div>
  <div class="line-y" style="left:35px;top:35px;width:2px;height:392px"></div>

  <h1 class="headline">
    <span class="small">WE OFFER</span>
    <span class="big">HOT AND COLD</span>
    <span class="big" style="margin-top:4px">EQUIPMENT</span>
    <span class="small last">REPAIR</span>
  </h1>
  <p class="intro">Installation, Rebuilds, OSHA Inspection,<br>and <em>Preventive Maintenance Services</em><br>for Denver Metro and Surrounding<br>Areas.</p>

  <div class="portrait" role="img" aria-label="Photo of a smiling technician in a hard hat and blue polo shirt"></div>

  <div class="photo" style="left:50px;top:460px;width:290px;height:190px;transform:rotate(-8deg)" role="img" aria-label="Stainless steel commercial kitchen"></div>
  <div class="photo" style="left:76px;top:675px;width:290px;height:180px;transform:rotate(10deg)" role="img" aria-label="Technician servicing a kitchen appliance"></div>
  <div class="photo" style="left:70px;top:877px;width:280px;height:170px;transform:rotate(-18deg)" role="img" aria-label="Technician repairing refrigeration equipment"></div>

  <h2 class="handle">WE HANDLE<br>EVERYTHING FROM THE FRONT<br>DOOR TO THE BACK DOOR</h2>
  <h2 class="offer-title">WE OFFER</h2>

  <div class="offer-item col-a" style="top:660px">HOT AND COLD<br>EQUIPMENT REPAIR<svg viewBox="0 0 20 20" aria-hidden="true"><rect x="1.5" y="3.5" width="15" height="15" fill="none" stroke="#1c1c1c" stroke-width="1.6"/><path d="M5 11l3.5 4L18 2" fill="none" stroke="#1c1c1c" stroke-width="2"/></svg></div>
  <div class="offer-item col-a" style="top:726px">CLEANING<svg viewBox="0 0 20 20" aria-hidden="true"><rect x="1.5" y="3.5" width="15" height="15" fill="none" stroke="#1c1c1c" stroke-width="1.6"/><path d="M5 11l3.5 4L18 2" fill="none" stroke="#1c1c1c" stroke-width="2"/></svg></div>
  <div class="offer-item col-a" style="top:771px">MAINTENANCE<svg viewBox="0 0 20 20" aria-hidden="true"><rect x="1.5" y="3.5" width="15" height="15" fill="none" stroke="#1c1c1c" stroke-width="1.6"/><path d="M5 11l3.5 4L18 2" fill="none" stroke="#1c1c1c" stroke-width="2"/></svg></div>
  <div class="offer-item col-a" style="top:816px">HANDYMAN WORK<svg viewBox="0 0 20 20" aria-hidden="true"><rect x="1.5" y="3.5" width="15" height="15" fill="none" stroke="#1c1c1c" stroke-width="1.6"/><path d="M5 11l3.5 4L18 2" fill="none" stroke="#1c1c1c" stroke-width="2"/></svg></div>

  <div class="offer-item col-b" style="top:637px">DRYWALL<svg viewBox="0 0 20 20" aria-hidden="true"><rect x="1.5" y="3.5" width="15" height="15" fill="none" stroke="#1c1c1c" stroke-width="1.6"/><path d="M5 11l3.5 4L18 2" fill="none" stroke="#1c1c1c" stroke-width="2"/></svg></div>
  <div class="offer-item col-b" style="top:682px">PAINTING<svg viewBox="0 0 20 20" aria-hidden="true"><rect x="1.5" y="3.5" width="15" height="15" fill="none" stroke="#1c1c1c" stroke-width="1.6"/><path d="M5 11l3.5 4L18 2" fill="none" stroke="#1c1c1c" stroke-width="2"/></svg></div>
  <div class="offer-item col-b" style="top:726px">DOOR CLOSERS<svg viewBox="0 0 20 20" aria-hidden="true"><rect x="1.5" y="3.5" width="15" height="15" fill="none" stroke="#1c1c1c" stroke-width="1.6"/><path d="M5 11l3.5 4L18 2" fill="none" stroke="#1c1c1c" stroke-width="2"/></svg></div>
  <div class="offer-item col-b" style="top:771px">FLOORS<svg viewBox="0 0 20 20" aria-hidden="true"><rect x="1.5" y="3.5" width="15" height="15" fill="none" stroke="#1c1c1c" stroke-width="1.6"/><path d="M5 11l3.5 4L18 2" fill="none" stroke="#1c1c1c" stroke-width="2"/></svg></div>
  <div class="offer-item col-b" style="top:816px">CEILING TILES<svg viewBox="0 0 20 20" aria-hidden="true"><rect x="1.5" y="3.5" width="15" height="15" fill="none" stroke="#1c1c1c" stroke-width="1.6"/><path d="M5 11l3.5 4L18 2" fill="none" stroke="#1c1c1c" stroke-width="2"/></svg></div>

  <h2 class="need" style="right:62px;top:903px"><span class="accent">FOR ANY NEED</span>IN YOUR RESTAURANT</h2>
  <div class="call-pill">CALL US</div>
  <p class="call-note">and we will send a skilled<br>technician to manage all your<br>commercial and industrial facility<br>requirements</p>

  <div class="line-k" style="left:839px;top:878px;width:2px;height:322px"></div>
  <div class="line-k" style="left:258px;top:1198px;width:583px;height:2px"></div>

  <div class="contact" style="left:52px;top:1104px">
    <svg viewBox="0 0 60 60" aria-hidden="true"><path d="M14 8l9 10-5 6c3 7 8 12 15 15l6-5 10 9-6 8C27 52 8 33 6 14z" fill="#f8d112"/><path d="M33 14a14 14 0 0 1 13 13M34 5a23 23 0 0 1 21 21" fill="none" stroke="#f8d112" stroke-width="3.5" stroke-linecap="round"/></svg>
    <div><span class="label">CALL TODAY :</span><span class="number">0123 456 789</span></div>
  </div>
</section>

<!-- SERVICES -->
<section class="flyer flyer--services">
  <svg class="backdrop" viewBox="0 0 880 1232" preserveAspectRatio="none" role="img" aria-label="Dimmed commercial kitchen photo behind the services list">
    <defs>
      <linearGradient id="back-dark" x1="0" y1="0" x2="1" y2="1">
        <stop offset="0" stop-color="#262626"/><stop offset="1" stop-color="#151515"/>
      </linearGradient>
    </defs>
    <rect width="880" height="1232" fill="url(#back-dark)"/>
    <polygon points="0,677 880,570 880,1000 0,1112" fill="#f8d112"/>
    <polygon points="0,1112 880,1000 880,1232 0,1232" fill="#ffffff"/>
  </svg>

  <div class="line-y" style="left:25px;top:53px;width:830px;height:2px"></div>
  <div class="line-y" style="left:25px;top:53px;width:2px;height:624px"></div>
  <div class="line-y" style="left:853px;top:53px;width:2px;height:522px"></div>
  <h2 class="services-pill">OUR SERVICES</h2>

  <ul class="service-list list-left">
    <li>Kitchex Certified Technicians</li>
    <li>Round-the-clock Emergency Services</li>
    <li>Customers Who Subscribe To<br>Preventive Maintenance Services<br>Receive A Reduced Rate On Hourly<br>Labor Charges.</li>
    <li>Original Equipment Manufacturer<br>(Oem) Parts</li>
    <li>30-day Warranty On All Oem<br>Parts Installed</li>
    <li>Equipment Cleaning &amp; Rebuilds</li>
    <li>Building Graffiti Removal Services</li>
    <li>Hot &amp; Cold Equipment</li>
  </ul>
  <ul class="service-list list-right">
    <li>Used Equipment Available For<br>Purchase Or Rental</li>
    <li>Specialized Programs<br>For Preventive Maintenance Of<br>Equipment</li>
    <li>Installation And<br>Repair Of Restaurant Equipment</li>
    <li>Repair Or Replace Restaurant<br>Furniture</li>
    <li>Comprehensive Licensed<br>Electrical Contractor Services For<br>Both Interior And Exterior Projects<br>Including Lighting System Upgrades</li>
    <li>Food Service Trucks</li>
  </ul>

  <div class="photo" style="left:55px;top:630px;width:360px;height:250px;transform:rotate(10deg)" role="img" aria-label="Commercial kitchen line with hanging utensils"></div>
  <div class="photo" style="left:82px;top:895px;width:330px;height:190px;transform:rotate(-15deg)" role="img" aria-label="Stainless steel restaurant kitchen"></div>

  <div class="repair-row" style="left:485px;top:642px"><svg viewBox="0 0 30 28" aria-hidden="true"><path d="M2 15l8 10L28 2" fill="none" stroke="#1c1c1c" stroke-width="4"/></svg>WE REPAIR FLOORS</div>
  <div class="repair-row" style="left:485px;top:694px"><svg viewBox="0 0 30 28" aria-hidden="true"><path d="M2 15l8 10L28 2" fill="none" stroke="#1c1c1c" stroke-width="4"/></svg>WALLS<span class="pair"><svg viewBox="0 0 30 28" aria-hidden="true"><path d="M2 15l8 10L28 2" fill="none" stroke="#1c1c1c" stroke-width="4"/></svg></span><span style="margin-left:-10px">COUNTERS</span></div>
  <div class="repair-row" style="left:485px;top:746px"><svg viewBox="0 0 30 28" aria-hidden="true"><path d="M2 15l8 10L28 2" fill="none" stroke="#1c1c1c" stroke-width="4"/></svg>DÉCOR<span class="pair"><svg viewBox="0 0 30 28" aria-hidden="true"><path d="M2 15l8 10L28 2" fill="none" stroke="#1c1c1c" stroke-width="4"/></svg></span><span style="margin-left:-10px">SIGNAGE</span></div>
  <div class="repair-row" style="left:485px;top:798px"><svg viewBox="0 0 30 28" aria-hidden="true"><path d="M2 15l8 10L28 2" fill="none" stroke="#1c1c1c" stroke-width="4"/></svg>PARKING LOTS</div>
  <div class="repair-row" style="left:485px;top:850px"><svg viewBox="0 0 30 28" aria-hidden="true"><path d="M2 15l8 10L28 2" fill="none" stroke="#1c1c1c" stroke-width="4"/></svg>DUMPSTERS</div>
  <div class="repair-row" style="left:485px;top:902px"><svg viewBox="0 0 30 28" aria-hidden="true"><path d="M2 15l8 10L28 2" fill="none" stroke="#1c1c1c" stroke-width="4"/></svg>AND MORE</div>
  <p class="fix-note">IF YOU HAVE IT WE PROBABLY<br>FIX IT.</p>

  <div class="contact" style="left:75px;top:1136px">
    <svg viewBox="0 0 60 60" aria-hidden="true"><path d="M14 8l9 10-5 6c3 7 8 12 15 15l6-5 10 9-6 8C27 52 8 33 6 14z" fill="#f8d112"/><path d="M33 14a14 14 0 0 1 13 13M34 5a23 23 0 0 1 21 21" fill="none" stroke="#f8d112" stroke-width="3.5" stroke-linecap="round"/></svg>
    <div><span class="label">CALL TODAY :</span><span class="number">0123 456 789</span></div>
  </div>
  <h2 class="need" style="right:52px;top:1098px"><span class="accent">FOR ANY NEED</span>IN YOUR RESTAURANT</h2>
</section>

</body>
</html>
```